Utah Iron Ridge Marketing Flyer

I need a 1 page flyer that will go in a magazine to advertise our youth sports club and the various sports we have teams for. I want to make sure we feature pictures of our teams, our logos for basketball and volleyball, our title logo from our website and most importantly, HOW TO CONTACT US by going to our website www.utahironridge.example

Target Market(s)

Youth Sports Club

Colors
85cae6

Requirements
Must have
• Use the colors from our website: Carolina blue, black and silver. Must use the info provided in the Word Document I provided. Must have in bold and enlarged lettering how to contact us by going to our website www.utahironridge.example

```html
<!DOCTYPE html>
<html lang="en">
<head>
<meta charset="utf-8">
<title>Utah Iron Ridge – Youth Sports Flyer</title>
<link rel="stylesheet" href="https://fonts.googleapis.com/css2?family=Carlito:wght@400;700&family=Russo+One&display=swap">
<style>
  :root {
    --carolina: #85cae6;
    --sky-text: #1fa8e0;
    --ink: #000000;
    --white: #ffffff;
    --silver: #c9cdd2;
    --footer-blue: #0a6fc2;
    --band-deep: #1d3fb8;
    --band-light: #5fd0f5;
    --frame: #1c3a44;
  }
  * { box-sizing: border-box; margin: 0; padding: 0; }
  html, body { width: 927px; height: 1200px; overflow: hidden; background: var(--ink); }
  .flyer {
    position: relative; width: 927px; height: 1200px; overflow: hidden;
    background: var(--ink); color: var(--white);
    font-family: "Carlito", "Calibri", sans-serif;
  }
  .title-rule { position: absolute; left: 0; right: 0; top: 106px; height: 1px; background: #5b6870; }
  .site-title {
    position: absolute; left: 0; right: 0; top: 74px; text-align: center;
    font-weight: 700; font-size: 66px; letter-spacing: 21px; padding-left: 21px; text-transform: uppercase;
    color: var(--carolina); line-height: 1;
  }

  .hero {
    position: absolute; left: 0; top: 210px; width: 927px; height: 432px;
    background:
      radial-gradient(ellipse 150px 230px at 95px 215px, rgba(133,202,230,0.55), rgba(133,202,230,0.18) 60%, rgba(133,202,230,0) 100%),
      radial-gradient(ellipse 120px 220px at 815px 225px, rgba(133,202,230,0.55), rgba(133,202,230,0.18) 60%, rgba(133,202,230,0) 100%),
      linear-gradient(180deg, rgba(0,0,0,0) 0%, rgba(0,0,0,0) 62%, rgba(10,14,18,0.85) 86%, #000 100%),
      linear-gradient(180deg, #4b6672 0%, #34505d 22%, #24363f 44%, #3a4a52 58%, #1c2a31 72%, #0b1216 100%);
  }
  .hero-lines {
    position: absolute; left: 0; top: 18px; width: 252px; height: 14px;
    border-top: 2px solid rgba(201,205,210,0.7);
    border-bottom: 2px solid rgba(201,205,210,0.55);
  }

  .club-mark {
    position: absolute; left: 264px; top: 262px; width: 400px; text-align: center;
  }
  .club-mark-dot {
    width: 150px; height: 150px; border-radius: 50%;
    background: var(--carolina);
    margin: 0 auto 22px;
  }
  .club-mark-name { font-weight: 700; font-size: 50px; color: var(--carolina); line-height: 1; }

  .intro {
    position: absolute; left: 0; right: 0; top: 609px; text-align: center;
    color: var(--sky-text); font-size: 21px; line-height: 30px;
  }
  .about {
    position: absolute; left: 0; right: 0; top: 698px; text-align: center;
    font-size: 21px; line-height: 29.5px; color: var(--white);
  }
  .about sup { font-size: 11px; vertical-align: 8px; line-height: 0; }

  .tryout { position: absolute; }
  .tryout-ball { position: absolute; left: 50%; transform: translateX(-50%); top: 0; }
  .tryout-head {
    position: absolute; left: 0; right: 0; display: flex; align-items: center; justify-content: center;
    text-align: center; font-family: "Russo One", sans-serif; text-transform: uppercase;
    color: var(--white); line-height: 1;
    background: linear-gradient(100deg, var(--band-deep) 0%, var(--band-light) 45%, var(--band-deep) 100%);
  }
  .tryout-when {
    position: absolute; left: 0; right: 0; bottom: 0; text-align: center;
    border: 1px solid var(--frame); border-top: none; font-size: 23px; color: var(--white);
    display: flex; align-items: center; justify-content: center; line-height: 31px;
  }
  .tryout--basketball { left: 65px; top: 862px; width: 202px; height: 172px; }
  .tryout--volleyball { left: 310px; top: 824px; width: 308px; height: 210px; }
  .tryout--softball { left: 660px; top: 862px; width: 202px; height: 172px; }
  .tryout--basketball .tryout-head, .tryout--softball .tryout-head { top: 72px; height: 62px; font-size: 17px; flex-direction: column; }
  .tryout--basketball .tryout-when, .tryout--softball .tryout-when { height: 38px; }
  .tryout--volleyball .tryout-head { top: 72px; height: 62px; font-size: 18px; letter-spacing: 1px; }
  .tryout--volleyball .tryout-when { height: 76px; }

  .footer-band {
    position: absolute; left: 0; right: 0; top: 1088px; height: 39px; background: var(--footer-blue);
    display: flex; align-items: center; justify-content: center; font-size: 23px; color: var(--white);
  }
  .footer-band strong { font-weight: 700; margin-left: 8px; }
</style>
</head>
<body>
<main class="flyer">
  <div class="title-rule"></div>
  <h1 class="site-title">Utah Iron Ridge</h1>

  <section class="hero" role="img" aria-label="Team photo montage: youth basketball players in light blue uniforms dribbling on both sides, in front of a city skyline at dusk with mountains behind">
    <div class="hero-lines"></div>
  </section>

  <div class="club-mark">
    <div class="club-mark-dot"></div>
    <div class="club-mark-name">Utah Iron Ridge</div>
  </div>

  <p class="intro">Utah Iron Ridge is a Layton,<br>Utah based Basketball, Volleyball &amp; Softball club</p>

  <p class="about">youth sports program for both boys and girls 2<sup>nd</sup> – 12<sup>th</sup> grades.<br>Teams range from Developmental to Premier Travel teams,<br>so if you're looking to improve your skills,<br>we can help.</p>

  <div class="tryout tryout--basketball">
    <svg class="tryout-ball" width="130" height="72" viewBox="0 0 130 72" aria-hidden="true">
      <defs><linearGradient id="ballBlueA" x1="0" y1="0" x2="1" y2="1"><stop offset="0" stop-color="#a9e3fb"/><stop offset="1" stop-color="#3fb4e6"/></linearGradient></defs>
      <path d="M0 72 A65 65 0 0 1 130 72 Z" fill="url(#ballBlueA)"/>
      <path d="M8 40 Q65 20 122 40" fill="none" stroke="#000" stroke-width="4"/>
      <path d="M80 9 Q64 40 92 72" fill="none" stroke="#000" stroke-width="4"/>
    </svg>
    <div class="tryout-head"><span>Basketball</span><span>Tryouts</span></div>
    <div class="tryout-when">End of August</div>
  </div>

  <div class="tryout tryout--volleyball">
    <svg class="tryout-ball" width="130" height="72" viewBox="0 0 130 72" aria-hidden="true">
      <defs><linearGradient id="ballBlueB" x1="0" y1="0" x2="1" y2="1"><stop offset="0" stop-color="#a9e3fb"/><stop offset="1" stop-color="#3fb4e6"/></linearGradient></defs>
      <path d="M0 72 A65 65 0 0 1 130 72 Z" fill="url(#ballBlueB)"/>
      <path d="M70 8 Q52 40 68 72" fill="none" stroke="#000" stroke-width="4"/>
      <path d="M95 18 Q84 44 96 72" fill="none" stroke="#000" stroke-width="4"/>
    </svg>
    <div class="tryout-head">Volleyball Tryouts</div>
    <div class="tryout-when">October for Jr. High /<br>November for High School</div>
  </div>

  <div class="tryout tryout--softball">
    <svg class="tryout-ball" width="130" height="72" viewBox="0 0 130 72" aria-hidden="true">
      <defs><linearGradient id="ballBlueC" x1="0" y1="0" x2="1" y2="1"><stop offset="0" stop-color="#a9e3fb"/><stop offset="1" stop-color="#3fb4e6"/></linearGradient></defs>
      <path d="M0 72 A65 65 0 0 1 130 72 Z" fill="url(#ballBlueC)"/>
      <path d="M78 8 Q112 26 122 64" fill="none" stroke="#000" stroke-width="4" stroke-dasharray="5 6"/>
    </svg>
    <div class="tryout-head"><span>Softball</span><span>Tryouts</span></div>
    <div class="tryout-when">July</div>
  </div>

  <footer class="footer-band">For more information, please visit our website: <strong>www.utahironridge.example</strong></footer>
</main>
</body>
</html>
```